Gentle threads

Organic ethical yoga/activewear that supports kids in need and other community projects by donating % of all sales to these causes. See the product and the brand (Wirra project) story and catalogue on
Gentlethreads.com.au
http://files.palmbrook.net/doc/k7rq2m_a41c93e7b20d4f58c61e8a9d3f027b6e.pdf
Flyer is for gentle threads as the distributor for Wirra clothing
Would like the flyer to be simple with core message and contact and site details but have a similar feel to the catalogue using some of the art graphics and or photo from site for colour. Also for wholesale/distributor enquiries or to arrange an appointment for a brand presentation contact Mara Lodge 0412
Updates
I have four that I am considering so please don't submit any more. One of these will be suitable. Thanks for your submissions.
Mara
Target Market(s)
Yoga studios, wellness centres , private parties, gyms, agents
Industry/Entity Type
Clothing
Look and feel
Each slider illustrates characteristics of the customer's brand and the style your logo design should communicate.

```html
<!DOCTYPE html>
<html lang="en">
<head>
<meta charset="utf-8">
<title>Wirra project – Flyer</title>
<link href="https://fonts.googleapis.com/css2?family=Cherry+Swash:wght@700&family=Delius&family=Rokkitt:wght@700&family=Amatic+SC:wght@400&display=swap" rel="stylesheet">
<style>
  :root {
    --page-bg: #e8e3df;
    --mauve: #9a5874;
    --mauve-pattern: #7e4259;
    --cream: #f2efe6;
    --sage: #b9c6c3;
    --plum-text: #4a1d31;
    --rose: #d27f97;
    --white: #ffffff;
  }
  * { margin: 0; padding: 0; box-sizing: border-box; }
  html, body {
    width: 1200px; height: 1000px; overflow: hidden;
    background: var(--page-bg);
  }
  .flyer {
    position: absolute; left: 60px; top: 152px;
    width: 930px; height: 600px;
    transform: scale(1.16); transform-origin: top left;
    overflow: hidden;
    background: var(--cream);
    box-shadow: 0 6px 20px rgba(0,0,0,0.18);
  }
  .flyer-art { position: absolute; inset: 0; width: 930px; height: 600px; }
  .brand-tile {
    position: absolute; left: 397px; top: 14px;
    width: 94px; height: 138px;
    background: var(--white); border-radius: 8px;
    display: flex; align-items: center; justify-content: center;
    text-align: center;
  }
  .brand-name {
    font-family: "Rokkitt", Georgia, serif; font-weight: 700;
    font-size: 19px; line-height: 1.1; color: #1a1a1a;
  }
  .core-title {
    position: absolute; left: 50px; top: 176px;
    font-family: "Cherry Swash", Georgia, serif; font-weight: 700;
    font-size: 24px; color: var(--plum-text); letter-spacing: 0.5px;
  }
  .core-body {
    position: absolute; left: 50px; top: 208px; width: 560px;
    font-family: "Delius", "Comic Sans MS", cursive;
    font-size: 14px; line-height: 25px; color: var(--plum-text);
  }
  .more-info {
    position: absolute; left: 52px; top: 485px;
    font-family: "Rokkitt", Georgia, serif; font-weight: 700;
    font-size: 16.5px; color: var(--plum-text);
  }
  .tagline {
    position: absolute; left: 607px; top: 140px; width: 150px;
    text-align: center; color: var(--white);
    font-family: "Amatic SC", "Arial Narrow", sans-serif;
    line-height: 1;
  }
  .tagline .small { font-size: 22px; display: block; }
  .tagline .large { font-size: 36px; display: block; }
  .tagline .dots { font-size: 24px; display: block; letter-spacing: 2px; }
  .trade-contact {
    position: absolute; left: 60px; top: 543px; width: 500px;
    font-family: "Rokkitt", Georgia, serif; font-weight: 700;
    font-size: 13.5px; line-height: 17px; color: var(--white);
  }
</style>
</head>
<body>
<main class="flyer">
  <svg class="flyer-art" viewBox="0 0 930 600">
    <defs>
      <clipPath id="flyer-clip"><rect width="930" height="600"/></clipPath>
    </defs>
    <g clip-path="url(#flyer-clip)">
      <rect class="top-band" x="0" y="0" width="930" height="170" fill="var(--mauve)"/>
      <rect class="bottom-band" x="0" y="517" width="930" height="83" fill="var(--mauve)"/>
      <polygon class="sage-panel" points="185,170 640,10 720,517 255,517" fill="var(--sage)" opacity="0.8"/>
      <rect x="0" y="170" width="185" height="347" fill="var(--cream)"/>
      <g role="img" aria-label="Zigzag and triangle pattern strips in deep mauve">
        <rect x="75" y="26" width="280" height="12" fill="var(--mauve-pattern)" opacity="0.55"/>
        <rect x="88" y="62" width="280" height="42" fill="var(--mauve-pattern)" opacity="0.45"/>
        <rect x="75" y="132" width="280" height="12" fill="var(--mauve-pattern)" opacity="0.55"/>
        <rect x="508" y="26" width="200" height="12" fill="var(--mauve-pattern)" opacity="0.55"/>
        <rect x="540" y="62" width="150" height="28" fill="var(--mauve-pattern)" opacity="0.45"/>
        <rect x="520" y="132" width="180" height="12" fill="var(--mauve-pattern)" opacity="0.55"/>
        <rect x="0" y="578" width="700" height="12" fill="var(--mauve-pattern)" opacity="0.45"/>
      </g>
      <g class="mosaic" stroke="var(--white)" stroke-width="5" stroke-linejoin="round">
        <polygon role="img" aria-label="Photo: children on a grassy mountain hillside under a cloudy sky" points="785,-3 888,100 785,203 682,100" fill="#a9b5bd"/>
        <polygon class="tagline-diamond" points="682,100 785,203 682,306 579,203" fill="var(--rose)"/>
        <polygon role="img" aria-label="Photo: pink painted village house with a doorway" points="888,100 991,203 888,306 785,203" fill="#c7788a"/>
        <polygon role="img" aria-label="Photo: close-up of red striped woven textile" points="579,203 682,306 579,409 476,306" fill="#c0485a"/>
        <polygon role="img" aria-label="Photo: young child in a green knitted hat" points="785,203 888,306 785,409 682,306" fill="#8c7a62"/>
        <polygon points="991,203 1094,306 991,409 888,306" fill="#6fa0c8"/>
        <polygon role="img" aria-label="Photo: girl in a white coat holding a small lamb" points="682,306 785,409 682,512 579,409" fill="#9a8d86"/>
        <polygon role="img" aria-label="Photo: hillside town with colourful houses" points="888,306 991,409 888,512 785,409" fill="#8d98a3"/>
        <polygon role="img" aria-label="Photo: woven rug with geometric motifs in brown tones" points="785,409 888,512 785,615 682,512" fill="#8a7261"/>
      </g>
    </g>
  </svg>

  <div class="brand-tile"><span class="brand-name">WIRRA<br>project</span></div>

  <div class="tagline">
    <span class="small">WE</span>
    <span class="large">TRAVEL</span>
    <span class="large">TO EXPLORE</span>
    <span class="dots">...</span>
  </div>

  <h1 class="core-title">OUR CORE MESSAGE</h1>
  <p class="core-body">
    wirra Project exists to encourage the creativity of children in<br>
    partnership with select charities in Peru. Their touching drawings<br>
    are turned into graphics used on wirra products. These<br>
    products are then sold to generate funds for these<br>
    charities to finance projects that allow the children to grow<br>
    up in a creative and safe environment. We are not only dedi-<br>
    cated to providing the children we sponsor with the freedom to<br>
    express themselves, but also strive to provide them with choices and<br>
    opportunities. By nourishing their creative skills, teaching them new artistic<br>
    techniques, and giving value to their work we hope to present art and design<br>
    as a potential path to change their life and future.
  </p>
  <p class="more-info">For More Information visit : www.wirraproject.com</p>

  <p class="trade-contact">For wholesale/distributor enquiries or to arrange an appointment for a brand presentation contact Mara Lodge 0412</p>
</main>
</body>
</html>
```